Design for "Vellow" protein health bars wrappers

I need a new design for a protein bar that my partners and I are launching for the North American and European markets.
The bar's name is "Vellow."
Given the masculine/aggressive nature of that name, we are thinking of neutralizing it with a more feminine/soft font and design. But hey - the sky is the limit. We obviously want this 20-gram protein bar to sell to a wide net (not just men but women also). So if it means having a Pellam Comic font/design (or whatever) in order to do this, so be it. I leave it up to your intelligence and experience.

ADDED ON FEBRUARY 24:

The official name of the bar is just "VELLOW" (not "Vellow Protein").

We have six flavors divided into two categories, which are 1) SOFT and 2) CRUNCHY.
So, the idea is to make two similar designs for the wrapper that still distinguish themselves from each other because one is 'soft' and the other is 'crunchy.'
Then, within each category, the idea is to have three color variations, designating the three flavors in each category.

Please look at the dimensions and examples of the generic wrapper designs that we already have (and which we find too generic), which I have uploaded.

Target Market(s)

North America - Brindle, Fair Harvest
Europe - Norway, Sweden, Denmark, Germany, France, Switzerland, Italy.

Industry/Entity Type

Nutrition

Logo Text

Vellow

Font styles to use
Serif
Decorative

Colors
fff6dc
f04a50

Requirements
Must have
• The title is "Vellow".
• We have six flavors divided into two categories, which are 1) SOFT and 2) CRUNCHY.
• You can work on the two different types of similar-but-different designs for the "soft" and for the "cruncy." Then it's just a question of color variations for each flavor.
• The flavors are:
• SOFT: 1) strawberry, 2) Chocolate brownie, 3) Cinnamon Crunch
• CRUNCY: 1) Peanut, 2) Lemon, 3) Coconut.
• On the side or at the bottom, there should be stated:
• "20 gm protein"
• "children friendly"
Nice to have
• Obvious: a design that catches the eye and inspires someone to buy the bar to eat it.
• Part of the design could include a photograph of the actual bar (you can use generic photos for that until we place a pic of the actual bar). Like 1/4th of the total surface (or even a little smaller).

```html
<!DOCTYPE html>
<html lang="en">
<head>
<meta charset="utf-8">
<title>Vellow protein bar wrappers</title>
<link rel="stylesheet" href="https://fonts.googleapis.com/css2?family=Anton&family=Caveat+Brush&family=Oswald:wght@500;600&display=swap">
<style>
  :root {
    --stage: #1c1c1c;
    --wrapper: #fbfbfb;
    --crimp: #dcdcdc;
    --crimp-line: #a9a9a9;
    --cinnamon-brand: #5a1d0e;
    --cinnamon-pill: #c89262;
    --strawberry-brand: #c8102e;
    --brownie-brand: #4a1712;
  }
  * { box-sizing: border-box; margin: 0; padding: 0; }
  html, body { width: 1200px; height: 1056px; overflow: hidden; }
  body {
    background: var(--stage);
    position: relative;
    font-family: "Oswald", sans-serif;
  }
  .wrapper {
    position: absolute;
    width: 840px;
    height: 250px;
    background: var(--wrapper);
    overflow: hidden;
    box-shadow: 0 12px 30px rgba(0,0,0,.45);
  }
  .wrapper--cinnamon { left: 170px; top: 40px; --brand: var(--cinnamon-brand); --pill: var(--cinnamon-pill); }
  .wrapper--strawberry { left: 70px; top: 380px; --brand: var(--strawberry-brand); --pill: var(--strawberry-brand); }
  .wrapper--brownie { left: 290px; top: 730px; --brand: var(--brownie-brand); --pill: var(--brownie-brand); }

  .crimp {
    position: absolute;
    top: 0; bottom: 0;
    width: 52px;
    background: repeating-linear-gradient(to bottom, var(--crimp) 0 4px, var(--crimp-line) 4px 5px);
  }
  .crimp--left { left: 0; }
  .crimp--right { right: 0; width: 24px; }

  .bar-photo {
    position: absolute;
    top: 0; bottom: 0;
    right: 24px;
    width: 230px;
    clip-path: polygon(28% 0, 100% 0, 100% 100%, 0 100%, 12% 62%, 6% 45%, 20% 22%);
  }
  .wrapper--cinnamon .bar-photo { background: linear-gradient(140deg, #a8623a, #6e3219 60%, #8c4a28); }
  .wrapper--strawberry .bar-photo { background: linear-gradient(140deg, #e6cf9a, #c99a55 50%, #d98a7a); }
  .wrapper--brownie .bar-photo { background: linear-gradient(140deg, #5a2a1c, #2f120b 60%, #4a1f14); }

  .brand {
    position: absolute;
    left: 120px;
    top: 18px;
    display: flex;
    align-items: center;
    gap: 16px;
  }
  .brand__dot {
    width: 46px; height: 46px;
    border-radius: 50%;
    background: var(--brand);
  }
  .brand__name {
    font-family: "Anton", sans-serif;
    font-size: 138px;
    line-height: 1;
    letter-spacing: 2px;
    color: var(--brand);
  }

  .flavor {
    position: absolute;
    left: 300px;
    top: 184px;
    padding: 2px 22px 4px;
    border-radius: 24px;
    background: var(--pill);
    color: #fff;
    font-family: "Caveat Brush", cursive;
    font-size: 34px;
    line-height: 1.1;
  }

  .badges {
    position: absolute;
    left: 196px;
    top: 184px;
    display: flex;
    gap: 4px;
  }
  .badge {
    width: 44px; height: 44px;
    border-radius: 50%;
    border: 2px solid var(--pill);
    color: var(--pill);
    display: flex;
    flex-direction: column;
    align-items: center;
    justify-content: center;
    text-align: center;
    font-size: 7px;
    font-weight: 600;
    line-height: 1.05;
    text-transform: uppercase;
  }
  .badge strong { font-size: 12px; }
  .badge svg { width: 9px; height: 8px; fill: var(--pill); margin-bottom: 1px; }
</style>
</head>
<body>

  <article class="wrapper wrapper--cinnamon">
    <div class="crimp crimp--left"></div>
    <div class="brand"><span class="brand__dot"></span><h1 class="brand__name">VELLOW</h1></div>
    <div class="badges">
      <div class="badge">Protein<strong>20 gr</strong></div>
      <div class="badge"><svg viewBox="0 0 10 9"><path d="M5 9 0 4A2.5 2.5 0 0 1 5 1a2.5 2.5 0 0 1 5 3z"/></svg>Children<br>friendly</div>
    </div>
    <p class="flavor">Cinnamon Crunch</p>
    <div class="bar-photo" role="img" aria-label="Photo of the cinnamon crunch bar, glazed cereal pieces"></div>
    <div class="crimp crimp--right"></div>
  </article>

  <article class="wrapper wrapper--strawberry">
    <div class="crimp crimp--left"></div>
    <div class="brand"><span class="brand__dot"></span><h1 class="brand__name">VELLOW</h1></div>
    <div class="badges">
      <div class="badge">Protein<strong>20 gr</strong></div>
      <div class="badge"><svg viewBox="0 0 10 9"><path d="M5 9 0 4A2.5 2.5 0 0 1 5 1a2.5 2.5 0 0 1 5 3z"/></svg>Children<br>friendly</div>
    </div>
    <p class="flavor">Strawberry</p>
    <div class="bar-photo" role="img" aria-label="Photo of the strawberry bar, nuts and dried strawberry pieces"></div>
    <div class="crimp crimp--right"></div>
  </article>

  <article class="wrapper wrapper--brownie">
    <div class="crimp crimp--left"></div>
    <div class="brand"><span class="brand__dot"></span><h1 class="brand__name">VELLOW</h1></div>
    <div class="badges">
      <div class="badge">Protein<strong>20 gr</strong></div>
      <div class="badge"><svg viewBox="0 0 10 9"><path d="M5 9 0 4A2.5 2.5 0 0 1 5 1a2.5 2.5 0 0 1 5 3z"/></svg>Children<br>friendly</div>
    </div>
    <p class="flavor">Chocolate Brownie</p>
    <div class="bar-photo" role="img" aria-label="Photo of the chocolate brownie bar, chocolate cereal balls"></div>
    <div class="crimp crimp--right"></div>
  </article>

</body>
</html>
```